TKB Roofing Flyer/Mailer to be used to market to Homeowners

We need to create a flyer than can double as a mailer for our roofing business and possibly be used as a door hanger as well. This flyer will advertise our roofing company in a professional way with pictures as well as clear and precise text about who we are and what we offer. We are open to this flyer being a bi-fold or even a tri-fold. There would need to be an area for address if used as a mailer. A majority of our company information can be found on our website at www.tkbroofing-example.com.

Target Market(s)

Home Owners

Industry/Entity Type

Construction

Colors
0255a3
ffffff

Requirements
Must have
• Professional design, pictures, text with info regarding our company. Website: www.tkbroofing-example.com

```html
<!DOCTYPE html>
<html lang="en">
<head>
<meta charset="utf-8">
<title>TKB Roofing – Bi-fold Mailer</title>
<link href="https://fonts.googleapis.com/css2?family=Montserrat:wght@500;700;800;900&family=Open+Sans:wght@400;600;700&display=swap" rel="stylesheet">
<style>
:root{
  --brand-blue:#0255a3;
  --bright-blue:#1e8fe0;
  --sky-blue:#5cb6f2;
  --navy:#0f1b2d;
  --navy-2:#17263d;
  --ink:#3a3f47;
  --paper:#ffffff;
  --stage:#eceff3;
}
*{box-sizing:border-box;margin:0;padding:0}
html,body{width:835px;height:1200px;overflow:hidden;background:var(--stage)}
body{font-family:"Open Sans",Arial,sans-serif;color:var(--ink);position:relative}
.spread{position:absolute;left:37px;width:760px;height:556px;display:flex;box-shadow:0 6px 18px rgba(15,27,45,.18)}
.spread--outside{top:30px}
.spread--inside{top:614px}
.panel{position:relative;width:380px;height:556px;background:var(--paper);overflow:hidden}
.panel + .panel{border-left:1px solid #e3e7ec}
.wave{position:absolute;left:0;width:380px;display:block}
.heading{font-family:"Montserrat",Arial,sans-serif;font-weight:800;color:var(--brand-blue);text-transform:uppercase}
.body-copy{font-size:8.5px;line-height:1.55}
.photo{position:absolute;background:linear-gradient(160deg,#9fb8cf 0%,#6f8aa3 45%,#4f6a57 100%)}
.photo--round{border-radius:50%;border:3px solid var(--paper);box-shadow:0 0 0 2px var(--bright-blue)}
.brand{display:flex;align-items:center;gap:7px}
.brand__mark{width:14px;height:14px;background:var(--brand-blue)}
.brand__name{font-family:"Open Sans",Arial,sans-serif;font-weight:700;color:var(--brand-blue)}
.brand--light .brand__mark{background:var(--paper)}
.brand--light .brand__name{color:var(--paper)}

/* back panel */
.who{position:absolute;left:28px;top:34px;width:324px}
.who .heading{font-size:15px;margin-bottom:10px}
.who .body-copy + .body-copy{margin-top:8px}
.who .call-line{font-family:"Montserrat",Arial,sans-serif;font-weight:700;font-size:10.5px;color:var(--brand-blue);margin-top:10px}
.who-photos{position:absolute;top:232px;left:0;width:380px;display:flex;justify-content:center;gap:16px}
.who-photos .photo{position:relative;width:92px;height:92px}
.contact{position:absolute;left:28px;top:400px;width:324px;display:flex;gap:22px;color:var(--paper)}
.contact .brand__name{font-size:17px}
.contact-list{list-style:none;font-size:8.5px;line-height:1.3}
.contact-list li{display:flex;align-items:center;gap:7px;margin-bottom:6px}
.contact-list svg{flex:none}
.mail-area{position:absolute;left:28px;top:500px;width:324px;height:30px;border:1px solid rgba(255,255,255,.35)}

/* front panel */
.cover-brand{position:absolute;top:36px;left:0;width:380px;justify-content:center}
.cover-brand .brand__mark{width:20px;height:20px}
.cover-brand .brand__name{font-size:30px;letter-spacing:1px}
.cover-photo{left:0;top:104px;width:380px;height:270px}
.cover-title{position:absolute;right:26px;top:404px;text-align:right;color:var(--paper);font-family:"Montserrat",Arial,sans-serif;font-weight:900;font-size:20px;line-height:1.15;text-transform:uppercase}
.cover-phone{position:absolute;right:0;top:478px;width:250px;height:40px;background:var(--bright-blue);color:var(--paper);display:flex;align-items:center;justify-content:flex-end;gap:8px;padding-right:26px;font-family:"Montserrat",Arial,sans-serif;font-weight:800;font-size:22px}

/* inside left */
.services-head{position:absolute;left:28px;top:96px}
.services-head .kicker{font-family:"Montserrat",Arial,sans-serif;font-weight:600;font-size:9px;color:var(--navy)}
.services-head .heading{font-size:18px}
.service-grid{position:absolute;left:28px;top:160px;width:324px;display:grid;grid-template-columns:1fr 1fr;gap:26px 20px}
.service__icon{width:30px;height:30px;border-radius:50%;background:var(--brand-blue);display:flex;align-items:center;justify-content:center;margin-bottom:6px}
.service__title{font-family:"Montserrat",Arial,sans-serif;font-weight:800;font-size:9.5px;color:var(--brand-blue);margin-bottom:3px}
.call-today{position:absolute;left:28px;top:506px;color:var(--paper);font-family:"Montserrat",Arial,sans-serif;font-weight:800;font-size:14px}

/* inside right */
.why-head{position:absolute;right:28px;top:40px;text-align:right}
.why-head .kicker{font-family:"Montserrat",Arial,sans-serif;font-weight:600;font-size:10px;color:var(--navy)}
.why-head .heading{font-size:18px}
.reasons{position:absolute;left:34px;top:104px;width:312px;display:grid;grid-template-columns:repeat(3,1fr);gap:12px 10px;list-style:none}
.reason{text-align:center;font-family:"Montserrat",Arial,sans-serif;font-weight:700;font-size:8px;color:var(--navy);text-transform:uppercase;line-height:1.25}
.reason__icon{width:34px;height:34px;margin:0 auto 5px;border:2px solid var(--brand-blue);border-radius:50%;display:flex;align-items:center;justify-content:center}
.project-photos{position:absolute;left:0;top:408px;width:380px;display:flex;justify-content:center;gap:10px}
.project-photos .photo{position:relative;width:80px;height:80px}
</style>
</head>
<body>

<!-- OUTSIDE SPREAD -->
<section class="spread spread--outside">

  <article class="panel panel--back">
    <div class="who">
      <h2 class="heading">Who We Are</h2>
      <p class="body-copy">TKB Roofing is a family owned roofing company serving Indianapolis and surrounding areas. We focus on quality materials, honest pricing and clear communication, so every homeowner knows exactly what to expect from the first inspection to the final cleanup.</p>
      <p class="call-line">Call our office at 317-555-0142 to schedule a free estimate</p>
      <p class="body-copy">Our crews are licensed, insured and trained to install and repair every major roofing system with care.</p>
    </div>

    <div class="who-photos">
      <div class="photo photo--round" role="img" aria-label="Photo of a home with a new roof"></div>
      <div class="photo photo--round" role="img" aria-label="Photo of a finished residential roof"></div>
      <div class="photo photo--round" role="img" aria-label="Photo of a house exterior and roofline"></div>
    </div>

    <svg class="wave" style="top:330px" height="226" viewBox="0 0 380 226" aria-hidden="true">
      <path d="M0 40 C110 0 260 70 380 20 L380 226 L0 226Z" fill="var(--bright-blue)"/>
      <path d="M0 56 C120 18 260 86 380 38 L380 226 L0 226Z" fill="var(--navy)"/>
      <rect x="0" y="210" width="380" height="16" fill="var(--bright-blue)"/>
    </svg>

    <div class="contact">
      <div class="brand brand--light"><span class="brand__mark"></span><span class="brand__name">TKB Roofing</span></div>
      <ul class="contact-list">
        <li><svg width="11" height="11" viewBox="0 0 24 24"><path fill="#5cb6f2" d="M6.6 10.8a15 15 0 006.6 6.6l2.2-2.2c.3-.3.7-.4 1-.2 1.1.4 2.3.6 3.6.6.6 0 1 .4 1 1V20c0 .6-.4 1-1 1A17 17 0 013 4c0-.6.4-1 1-1h3.5c.6 0 1 .4 1 1 0 1.3.2 2.5.6 3.6.1.3 0 .7-.2 1z"/></svg>317-555-0142</li>
        <li><svg width="11" height="11" viewBox="0 0 24 24"><circle cx="12" cy="12" r="9" fill="none" stroke="#5cb6f2" stroke-width="2"/><path d="M3 12h18M12 3c3 3 3 15 0 18M12 3c-3 3-3 15 0 18" fill="none" stroke="#5cb6f2" stroke-width="1.6"/></svg>www.tkbroofing-example.com</li>
        <li><svg width="11" height="11" viewBox="0 0 24 24"><rect x="3" y="5" width="18" height="14" fill="none" stroke="#5cb6f2" stroke-width="2"/><path d="M3 6l9 7 9-7" fill="none" stroke="#5cb6f2" stroke-width="2"/></svg>info@tkbroofing-example.com</li>
        <li><svg width="11" height="11" viewBox="0 0 24 24"><path fill="#5cb6f2" d="M12 2a7 7 0 00-7 7c0 5 7 13 7 13s7-8 7-13a7 7 0 00-7-7zm0 9.5A2.5 2.5 0 1112 6a2.5 2.5 0 010 5.5z"/></svg>1200 Example Ave, Indianapolis, IN</li>
        <li><svg width="11" height="11" viewBox="0 0 24 24"><circle cx="12" cy="12" r="9" fill="none" stroke="#5cb6f2" stroke-width="2"/><path d="M12 7v5l3 3" fill="none" stroke="#5cb6f2" stroke-width="2"/></svg>Mon - Fri 8:00 AM - 5:00 PM</li>
      </ul>
    </div>
    <div class="mail-area" aria-label="Mailing address area"></div>
  </article>

  <article class="panel panel--front">
    <div class="brand cover-brand"><span class="brand__mark"></span><span class="brand__name">TKB Roofing</span></div>
    <div class="photo cover-photo" role="img" aria-label="Photo of a two-storey home with a new shingle roof and front yard"></div>
    <svg class="wave" style="top:340px" height="216" viewBox="0 0 380 216" aria-hidden="true">
      <path d="M0 30 C120 70 250 -10 380 22 L380 216 L0 216Z" fill="var(--bright-blue)"/>
      <path d="M0 46 C120 86 250 8 380 40 L380 216 L0 216Z" fill="var(--navy)"/>
      <rect x="0" y="196" width="380" height="20" fill="var(--brand-blue)"/>
    </svg>
    <h1 class="cover-title">Indy's Premier Roofing<br>Contractors</h1>
    <div class="cover-phone">
      <svg width="16" height="16" viewBox="0 0 24 24"><path fill="#fff" d="M6.6 10.8a15 15 0 006.6 6.6l2.2-2.2c.3-.3.7-.4 1-.2 1.1.4 2.3.6 3.6.6.6 0 1 .4 1 1V20c0 .6-.4 1-1 1A17 17 0 013 4c0-.6.4-1 1-1h3.5c.6 0 1 .4 1 1 0 1.3.2 2.5.6 3.6.1.3 0 .7-.2 1z"/></svg>
      317-555-0142
    </div>
  </article>
</section>

<!-- INSIDE SPREAD -->
<section class="spread spread--inside">

  <article class="panel panel--services">
    <svg class="wave" style="top:0" height="90" viewBox="0 0 380 90" aria-hidden="true">
      <path d="M0 0 H380 V40 C260 80 120 10 0 60Z" fill="var(--bright-blue)"/>
      <path d="M0 0 H380 V26 C260 64 120 -4 0 44Z" fill="var(--navy)"/>
    </svg>
    <div class="services-head">
      <p class="kicker">Residential &amp; Commercial</p>
      <h2 class="heading">Roofing Services</h2>
    </div>
    <div class="service-grid">
      <div class="service">
        <div class="service__icon"><svg width="16" height="16" viewBox="0 0 24 24"><path d="M3 12l9-8 9 8M6 10v10h12V10" fill="none" stroke="#fff" stroke-width="2"/></svg></div>
        <h3 class="service__title">ROOF REPLACEMENT</h3>
        <p class="body-copy">Complete tear off and new roof installed with durable, long lasting shingles.</p>
      </div>
      <div class="service">
        <div class="service__icon"><svg width="16" height="16" viewBox="0 0 24 24"><path d="M5 13l4 4L19 7" fill="none" stroke="#fff" stroke-width="2.5"/></svg></div>
        <h3 class="service__title">ROOF REPAIR</h3>
        <p class="body-copy">Fast fixes for leaks, missing shingles and worn flashing before damage spreads.</p>
      </div>
      <div class="service">
        <div class="service__icon"><svg width="16" height="16" viewBox="0 0 24 24"><path d="M13 2L5 14h6l-1 8 8-12h-6z" fill="#fff"/></svg></div>
        <h3 class="service__title">STORM DAMAGE REPAIR</h3>
        <p class="body-copy">Hail and wind damage inspections with help filing your insurance claim.</p>
      </div>
      <div class="service">
        <div class="service__icon"><svg width="16" height="16" viewBox="0 0 24 24"><rect x="4" y="5" width="16" height="14" fill="none" stroke="#fff" stroke-width="2"/><path d="M4 10h16M4 14h16" stroke="#fff" stroke-width="2"/></svg></div>
        <h3 class="service__title">GUTTERS &amp; SIDING</h3>
        <p class="body-copy">Seamless gutters and siding that protect and finish the whole home.</p>
      </div>
    </div>
    <svg class="wave" style="top:470px" height="86" viewBox="0 0 380 86" aria-hidden="true">
      <path d="M0 10 C120 -6 260 40 380 14 V86 H0Z" fill="var(--bright-blue)"/>
      <path d="M0 24 C120 8 260 54 380 28 V86 H0Z" fill="var(--navy)"/>
    </svg>
    <p class="call-today">Call Today - 317-555-0142</p>
  </article>

  <article class="panel panel--why">
    <div class="why-head">
      <p class="kicker">Why Choose</p>
      <h2 class="heading">TKB Roofing?</h2>
    </div>
    <ul class="reasons">
      <li class="reason"><div class="reason__icon"><svg width="16" height="16" viewBox="0 0 24 24"><path d="M5 13l4 4L19 7" fill="none" stroke="#0255a3" stroke-width="2.5"/></svg></div>Licensed &amp; Insured</li>
      <li class="reason"><div class="reason__icon"><svg width="16" height="16" viewBox="0 0 24 24"><path d="M5 13l4 4L19 7" fill="none" stroke="#0255a3" stroke-width="2.5"/></svg></div>Free Estimates</li>
      <li class="reason"><div class="reason__icon"><svg width="16" height="16" viewBox="0 0 24 24"><path d="M3 12l9-8 9 8M6 10v10h12V10" fill="none" stroke="#0255a3" stroke-width="2"/></svg></div>Quality Materials</li>
      <li class="reason"><div class="reason__icon"><svg width="16" height="16" viewBox="0 0 24 24"><path fill="#0255a3" d="M12 2a7 7 0 00-7 7c0 5 7 13 7 13s7-8 7-13a7 7 0 00-7-7zm0 9.5A2.5 2.5 0 1112 6a2.5 2.5 0 010 5.5z"/></svg></div>Local Experts</li>
      <li class="reason"><div class="reason__icon"><svg width="16" height="16" viewBox="0 0 24 24"><path d="M13 2L5 14h6l-1 8 8-12h-6z" fill="#0255a3"/></svg></div>Storm Damage Help</li>
      <li class="reason"><div class="reason__icon"><svg width="16" height="16" viewBox="0 0 24 24"><rect x="5" y="3" width="14" height="18" fill="none" stroke="#0255a3" stroke-width="2"/><path d="M8 8h8M8 12h8M8 16h5" stroke="#0255a3" stroke-width="2"/></svg></div>Insurance Claims</li>
      <li class="reason"><div class="reason__icon"><svg width="16" height="16" viewBox="0 0 24 24"><path d="M12 2l8 4v6c0 5-4 9-8 10-4-1-8-5-8-10V6z" fill="none" stroke="#0255a3" stroke-width="2"/></svg></div>Warranty Backed</li>
      <li class="reason"><div class="reason__icon"><svg width="16" height="16" viewBox="0 0 24 24"><path d="M5 13l4 4L19 7" fill="none" stroke="#0255a3" stroke-width="2.5"/></svg></div>Clean Job Sites</li>
      <li class="reason"><div class="reason__icon"><svg width="16" height="16" viewBox="0 0 24 24"><circle cx="12" cy="12" r="9" fill="none" stroke="#0255a3" stroke-width="2"/><path d="M12 7v5l3 3" fill="none" stroke="#0255a3" stroke-width="2"/></svg></div>On-Time Service</li>
      <li class="reason"><div class="reason__icon"><svg width="16" height="16" viewBox="0 0 24 24"><path d="M12 3v18M16 7H10a3 3 0 000 6h4a3 3 0 010 6H8" fill="none" stroke="#0255a3" stroke-width="2"/></svg></div>Fair Pricing</li>
      <li class="reason"><div class="reason__icon"><svg width="16" height="16" viewBox="0 0 24 24"><path d="M3 12l9-8 9 8M6 10v10h12V10" fill="none" stroke="#0255a3" stroke-width="2"/></svg></div>Trained Crews</li>
      <li class="reason"><div class="reason__icon"><svg width="16" height="16" viewBox="0 0 24 24"><path d="M12 20s-8-5-8-11a4 4 0 018-1 4 4 0 018 1c0 6-8 11-8 11z" fill="none" stroke="#0255a3" stroke-width="2"/></svg></div>Happy Homeowners</li>
    </ul>
    <svg class="wave" style="top:440px" height="116" viewBox="0 0 380 116" aria-hidden="true">
      <path d="M0 30 C130 0 250 60 380 26 V116 H0Z" fill="var(--bright-blue)"/>
      <path d="M0 46 C130 16 250 76 380 42 V116 H0Z" fill="var(--navy)"/>
    </svg>
    <div class="project-photos">
      <div class="photo photo--round" role="img" aria-label="Photo of a completed roofing project"></div>
      <div class="photo photo--round" role="img" aria-label="Photo of a home with new shingles"></div>
      <div class="photo photo--round" role="img" aria-label="Photo of a suburban house roof"></div>
      <div class="photo photo--round" role="img" aria-label="Photo of a brick home with a new roof"></div>
    </div>
  </article>
</section>

</body>
</html>
```